GLFH Social Media Layouts

Our client needs a social media layouts for a personal injury law firm based in Baltimore, Maryland. We've attached the logo we recently had created (but is not in use). The law firm is undergoing a complete rebrand. We would like to see options facebook layouts, but they will also be needing image sizes for linkedin, twitter and instagram.

```html
<!DOCTYPE html>
<html lang="en">
<head>
<meta charset="utf-8">
<title>GLFH Law – Personal Injury Social Layout</title>
<link rel="stylesheet" href="https://fonts.googleapis.com/css2?family=Oswald:wght@400;500&family=PT+Serif:wght@400;700&display=swap">
<style>
  :root {
    --navy: #1a2248;
    --navy-deep: #141b3b;
    --gold: #e9c84b;
    --white: #ffffff;
    --muted: #c9cde0;
    --photo-light: #d9c3a4;
    --photo-mid: #8a6a4c;
    --photo-book: #233060;
  }
  html, body {
    margin: 0;
    padding: 0;
    width: 800px;
    height: 1200px;
    overflow: hidden;
    background: var(--navy);
  }
  .post {
    position: relative;
    width: 800px;
    height: 1200px;
    background: var(--navy);
    overflow: hidden;
    font-family: "Oswald", sans-serif;
    color: var(--white);
  }
  .hero-photo {
    position: absolute;
    left: 0;
    top: 0;
    width: 800px;
    height: 660px;
    background:
      radial-gradient(ellipse at 15% 8%, #f3e6d2 0%, rgba(243,230,210,0) 40%),
      linear-gradient(160deg, var(--photo-light) 0%, var(--photo-mid) 30%, var(--photo-book) 48%, var(--navy-deep) 100%);
  }
  .hero-curve {
    position: absolute;
    left: 0;
    top: 440px;
    width: 800px;
    height: 240px;
  }
  .availability {
    position: absolute;
    left: 48px;
    top: 672px;
    margin: 0;
    font-weight: 400;
    font-size: 37px;
    line-height: 48px;
    letter-spacing: 0.5px;
    text-transform: uppercase;
  }
  .divider {
    position: absolute;
    left: 48px;
    right: 48px;
    height: 2px;
    background: var(--gold);
  }
  .divider--top { top: 790px; }
  .divider--bottom { top: 1052px; background: rgba(255,255,255,0.35); height: 1px; }
  .headline {
    position: absolute;
    left: 48px;
    top: 810px;
    margin: 0;
    font-family: "PT Serif", serif;
    font-weight: 400;
    font-size: 52px;
    line-height: 62px;
    text-transform: uppercase;
    color: var(--white);
  }
  .headline .accent { color: var(--gold); }
  .firm-mark {
    position: absolute;
    left: 48px;
    top: 1076px;
    display: flex;
    flex-direction: column;
    gap: 6px;
  }
  .firm-name {
    display: flex;
    align-items: center;
    gap: 14px;
    font-family: "PT Serif", serif;
    font-weight: 400;
    font-size: 58px;
    line-height: 1;
    color: var(--white);
    letter-spacing: 2px;
  }
  .firm-name .square {
    width: 16px;
    height: 16px;
    background: var(--white);
  }
  .firm-legal {
    font-family: "PT Serif", serif;
    font-size: 14px;
    color: var(--muted);
    letter-spacing: 0.5px;
    text-transform: uppercase;
  }
  .contact {
    position: absolute;
    left: 420px;
    top: 1090px;
    font-family: "PT Serif", serif;
    font-size: 27px;
    line-height: 38px;
    text-transform: uppercase;
    color: var(--white);
  }
</style>
</head>
<body>
  <main class="post">
    <div class="hero-photo" role="img" aria-label="Personal injury law book with a stethoscope resting on a desk"></div>
    <svg class="hero-curve" viewBox="0 0 800 240" preserveAspectRatio="none" aria-hidden="true">
      <path d="M0 30 C 140 150, 420 215, 800 215 L 800 240 L 0 240 Z" fill="var(--navy)"/>
      <path d="M0 30 C 140 150, 420 215, 800 215" fill="none" stroke="var(--gold)" stroke-width="5"/>
    </svg>

    <p class="availability">An attorney is available<br>7 days a week/24 hours a day</p>

    <div class="divider divider--top"></div>

    <h1 class="headline"><span class="accent">Helping injury</span><br>victims in Baltimore<br>and Maryland</h1>

    <div class="divider divider--bottom"></div>

    <div class="firm-mark">
      <div class="firm-name"><span class="square"></span>GLFH LAW</div>
      <div class="firm-legal">Garland, Lowry, Fenwick &amp; Hale, P.A.</div>
    </div>

    <div class="contact">
      Baltimore / Upper<br>
      Toll free 877-555-0142
    </div>
  </main>
</body>
</html>
```